New DermaLoom logo and packaging

We would like a new design for our new product DermaLoom, a high strength vitamin C serum which treats pigmentation. The packaging will reflect a high quality, clinical product with the logo "DermaLoom" on the front, with it's ingredients "Vitamin C, B3, B5, E and ferulic acid" the products are in two sizes 10ml and 30ml.

This is one of many products to come out in the DermaLoom range.

It would be for high end medical clinics selling premium brands, with a strong medical and clinical feel, professional and current or even futuristic in appearance.

Gold, blue, silver, White, cream are all colours that do this (without appearing cheap)

The product is not tested on animals, so would have
- "Not tested on animals".
- "12m" symbol for shelf life,
- "Made in USA"
- and ingredients list

See attached the product and existing box

Target Market(s)

Medical and aesthetic clinics

Font styles to use
Serif
Sans Serif

Colors
33a6d7
cee9f5
ffffff
fbed22
fee18a

Requirements
Must have
• High end premium brand
Nice to have
• like the idea of gold and silver lettering on cream background
Should not have
• Tacky, over complicated design

```html
<!DOCTYPE html>
<html lang="en">
<head>
<meta charset="utf-8">
<title>DermaLoom Vitamin C Serum – Packaging</title>
<link rel="stylesheet" href="https://fonts.googleapis.com/css2?family=Barlow+Condensed:wght@400;500&family=Montserrat:wght@400;500;800&display=swap">
<style>
  :root {
    --backdrop: #cdd6d7;
    --blush: #ecbba8;
    --blush-light: #f1c9b9;
    --gold: #a8802f;
    --gold-deep: #9a7428;
    --ink: #1f1a17;
    --white: #ffffff;
  }
  html, body {
    margin: 0;
    padding: 0;
    width: 1200px;
    height: 1149px;
    overflow: hidden;
    background: var(--backdrop);
  }
  .canvas {
    position: relative;
    width: 1200px;
    height: 1149px;
  }
  .panel {
    position: absolute;
    box-sizing: border-box;
    background: linear-gradient(160deg, var(--blush-light), var(--blush));
    display: flex;
    flex-direction: column;
    align-items: center;
    color: var(--gold);
    overflow: hidden;
  }
  .box-front {
    left: 166px;
    top: 158px;
    width: 390px;
    height: 774px;
  }
  .bottle-label {
    left: 596px;
    top: 486px;
    width: 242px;
    height: 426px;
  }
  .strength {
    font-family: "Barlow Condensed", sans-serif;
    font-weight: 500;
    margin: 0;
    line-height: 1;
  }
  .strength-sub {
    font-family: "Montserrat", sans-serif;
    font-weight: 400;
    margin: 0;
    line-height: 1;
  }
  .brand-name {
    font-family: "Montserrat", sans-serif;
    font-weight: 400;
    color: var(--white);
    margin: 0;
    line-height: 1;
    white-space: nowrap;
  }
  .product-block {
    box-sizing: border-box;
    border: 2px solid var(--gold);
    display: flex;
    flex-direction: column;
    align-items: stretch;
  }
  .product-title {
    font-family: "Montserrat", sans-serif;
    font-weight: 800;
    text-align: center;
    margin: 0;
    line-height: 1;
    white-space: nowrap;
  }
  .product-type {
    background: var(--gold-deep);
    color: var(--white);
    font-family: "Montserrat", sans-serif;
    font-weight: 400;
    text-align: center;
    margin: 0;
    line-height: 1;
    white-space: nowrap;
  }
  .ingredients {
    font-family: "Barlow Condensed", sans-serif;
    font-weight: 400;
    text-align: center;
    margin: 0;
    line-height: 1.15;
  }
  .volume {
    font-family: "Barlow Condensed", sans-serif;
    font-weight: 400;
    color: var(--ink);
    margin: 0;
    line-height: 1;
    white-space: nowrap;
  }

  /* box front sizing */
  .box-front .strength { font-size: 42px; margin-top: 74px; }
  .box-front .strength-sub { font-size: 17px; letter-spacing: 3px; margin-top: 8px; }
  .box-front .brand-name { font-size: 48px; margin-top: 78px; }
  .box-front .product-block { width: 290px; margin-top: 80px; }
  .box-front .product-title { font-size: 44px; letter-spacing: -1px; padding: 20px 0 17px; }
  .box-front .product-type { font-size: 27px; letter-spacing: 22px; padding: 11px 0 11px 22px; }
  .box-front .ingredients { font-size: 31px; margin-top: 66px; }
  .box-front .ingredients span { font-size: 25px; display: block; }
  .box-front .volume { font-size: 27px; margin-top: 72px; }

  /* bottle label sizing */
  .bottle-label .strength { font-size: 26px; margin-top: 38px; }
  .bottle-label .strength-sub { font-size: 11px; letter-spacing: 2px; margin-top: 4px; }
  .bottle-label .brand-name { font-size: 30px; margin-top: 42px; }
  .bottle-label .product-block { width: 214px; margin-top: 38px; }
  .bottle-label .product-title { font-size: 31px; letter-spacing: -0.5px; padding: 10px 0 6px; }
  .bottle-label .product-type { font-size: 16px; letter-spacing: 17px; padding: 5px 0 5px 17px; }
  .bottle-label .ingredients { font-size: 17px; margin-top: 40px; font-family: "Montserrat", sans-serif; }
  .bottle-label .ingredients span { font-size: 12px; display: block; }
  .bottle-label .volume { font-size: 14px; margin-top: 46px; font-family: "Montserrat", sans-serif; }
</style>
</head>
<body>
<main class="canvas">
  <section class="panel box-front" aria-label="Carton front panel">
    <h2 class="strength">HIGH STRENGTH</h2>
    <p class="strength-sub">VITAMIN C SERUM</p>
    <h1 class="brand-name">DermaLoom</h1>
    <div class="product-block">
      <p class="product-title">VITAMIN C</p>
      <p class="product-type">SERUM</p>
    </div>
    <p class="ingredients">Vitamin C, B3, B5, E<span>and ferulic acid</span></p>
    <p class="volume">30ML | 1FL. OZ</p>
  </section>

  <section class="panel bottle-label" aria-label="Bottle label">
    <h2 class="strength">HIGH STRENGTH</h2>
    <p class="strength-sub">VITAMIN C SERUM</p>
    <p class="brand-name">DermaLoom</p>
    <div class="product-block">
      <p class="product-title">VITAMIN C</p>
      <p class="product-type">SERUM</p>
    </div>
    <p class="ingredients">Vitamin C, B3, B5, E<span>and ferulic acid</span></p>
    <p class="volume">30ML | 1FL. OZ</p>
  </section>
</main>
</body>
</html>
```